Red Gum Business Card Design

We are a new small business specialising in under ground cable jointing and excavation works in NSW Australia.
Design I'm looking for is incorporating the Australian flag & excavator with out being to cheesy.
Maybe a faded washed out flag to help with overload of colour? & so its not the main focus.
Very open to creative out of the box designs!

Target Market(s)

Building & Construction

Industry/Entity Type

Construction

Contact Information for Business Card

Red Gum Cable Jointing & Excavations
Owen Falkirk

Ph: 0438 605 312
E: owen.falkirk@tallmail.example

Reverse Side
Services we offer:
High Voltage & Low Voltage Cable Jointing
Polymeric & paperlead jointing & terminations
Trenching & Auger Drilling 150 - 600mm
Site preparation / leveling / clearing
Driveway / Footpath / Turf Prep
Rubbish Removal
Tree & Stump removal
Footings & Post holes
Drainage
Service Installs
Gravels & Sands available
Any general Earth moving needs
Reliable Free Quotes
Fully Insured

Font styles to use
Serif
Script

Requirements
Nice to have
• small excavator (See uploaded picture)

```html
<!DOCTYPE html>
<html lang="en">
<head>
<meta charset="utf-8">
<title>Red Gum Business Card Design</title>
<link href="https://fonts.googleapis.com/css2?family=Ubuntu:wght@500&family=Marcellus+SC&family=Delius&display=swap" rel="stylesheet">
<style>
  :root{
    --navy:#23306e;
    --red:#d3253a;
    --white:#ffffff;
    --paper:#eef0f4;
    --ink:#2b3a86;
    --rule:#3b4a8e;
    --icon:#c9cde0;
  }
  *{box-sizing:border-box;margin:0;padding:0}
  html,body{width:1200px;height:952px;overflow:hidden;background:var(--paper)}
  .canvas{position:relative;width:1200px;height:952px}
  .card{position:absolute;left:290px;width:620px;height:360px;border-radius:30px;overflow:hidden;background:var(--white);box-shadow:0 8px 24px rgba(20,30,70,.18)}
  .card--front{top:80px}
  .card--back{top:500px}
  .band{position:absolute;left:0;width:100%}
  .band--navy{background:var(--navy)}
  .band--red{background:var(--red)}
  .flag-field{position:absolute;left:0;top:0;background:linear-gradient(90deg,#c75b6d 0%,#e9c9cf 45%,#9aa6cf 100%);opacity:.85}
  .stars{position:absolute;top:0;left:0}
  .brand{position:absolute;display:flex;align-items:center;gap:14px}
  .brand-mark{width:48px;height:48px;border-radius:50%;background:var(--navy);flex:none}
  .brand-name{font-family:'Ubuntu',sans-serif;font-weight:500;line-height:1.2}
  .brand-name--front{color:var(--navy);font-size:26px;width:330px}
  .brand-name--back{color:var(--white);font-size:18px;width:220px}
  .holder{position:absolute;left:0;width:100%;text-align:center;font-family:'Marcellus SC',serif;color:var(--white);font-size:28px;letter-spacing:1px;line-height:44px}
  .contact{position:absolute;display:flex;align-items:center;gap:14px;font-family:'Ubuntu',sans-serif;font-weight:500;color:var(--white);font-size:17px}
  .contact svg{flex:none}
  .services-title{position:absolute;left:26px;top:98px;font-family:'Delius',cursive;color:var(--red);font-size:19px}
  .services-rule{position:absolute;left:172px;top:120px;width:408px;height:1px;background:var(--rule)}
  .services{position:absolute;list-style:none;font-family:'Delius',cursive;color:var(--ink);font-size:13.5px;line-height:17px}
  .services li{position:relative;padding-left:18px}
  .services li::before{content:"";position:absolute;left:2px;top:4px;border-left:9px solid var(--red);border-top:5px solid transparent;border-bottom:5px solid transparent}
  .services--left{left:28px;top:128px}
  .services--right{left:350px;top:142px}
</style>
</head>
<body>
<main class="canvas">

  <section class="card card--front">
    <div class="band band--navy" style="top:0;height:72px"></div>
    <div class="flag-field" role="img" aria-label="Faded Australian flag canton" style="width:140px;height:72px"></div>
    <svg class="stars" width="620" height="72" viewBox="0 0 620 72" aria-hidden="true">
      <g fill="#ffffff">
        <polygon points="232,10 234.5,16 241,16.5 236,20.5 237.5,27 232,23.5 226.5,27 228,20.5 223,16.5 229.5,16"/>
        <polygon points="190,36 192.5,42 199,42.5 194,46.5 195.5,53 190,49.5 184.5,53 186,46.5 181,42.5 187.5,42"/>
      </g>
    </svg>
    <div class="band band--red" style="top:72px;height:3px"></div>

    <div class="brand" style="left:120px;top:112px">
      <div class="brand-mark"></div>
      <div class="brand-name brand-name--front">Red Gum Cable Jointing &amp; Excavations</div>
    </div>

    <div class="band band--red" style="top:216px;height:44px"></div>
    <div class="holder" style="top:216px">Owen Falkirk</div>
    <div class="band band--navy" style="top:260px;height:100px"></div>

    <div class="contact" style="left:46px;top:296px">
      <svg width="22" height="18" viewBox="0 0 22 18" aria-hidden="true"><path d="M2 5 Q11 -1 20 5 L18 8 L15 6 L7 6 L4 8 Z M5 9 H17 L19 17 H3 Z" fill="var(--icon)"/></svg>
      <span>0438 605 312</span>
    </div>
    <div class="contact" style="left:320px;top:276px">
      <svg width="24" height="16" viewBox="0 0 24 16" aria-hidden="true"><rect x="1" y="1" width="22" height="14" fill="var(--icon)"/><path d="M1 1 L12 9 L23 1" fill="none" stroke="var(--navy)" stroke-width="1.5"/></svg>
      <span>owen.falkirk@tallmail.example</span>
    </div>
  </section>

  <section class="card card--back">
    <div class="band band--navy" style="top:0;height:84px"></div>
    <div class="flag-field" role="img" aria-label="Faded Australian flag canton" style="width:170px;height:60px;top:6px"></div>
    <svg class="stars" width="620" height="84" viewBox="0 0 620 84" aria-hidden="true">
      <g fill="#ffffff">
        <polygon points="250,12 252.5,18 259,18.5 254,22.5 255.5,29 250,25.5 244.5,29 246,22.5 241,18.5 247.5,18"/>
        <polygon points="210,50 212.5,56 219,56.5 214,60.5 215.5,67 210,63.5 204.5,67 206,60.5 201,56.5 207.5,56"/>
      </g>
    </svg>
    <div class="brand" style="left:300px;top:20px;gap:10px">
      <div class="brand-mark" style="width:36px;height:36px;background:var(--white)"></div>
      <div class="brand-name brand-name--back">Red Gum Cable Jointing &amp; Excavations</div>
    </div>
    <div class="band band--red" style="top:84px;height:3px"></div>

    <div class="services-title">Services we offer:</div>
    <div class="services-rule"></div>
    <ul class="services services--left">
      <li>High Voltage &amp; Low Voltage Cable Jointing</li>
      <li>Polymeric &amp; paperlead jointing &amp; terminations</li>
      <li>Trenching &amp; Auger Drilling 150 - 600mm</li>
      <li>Site preparation / leveling / clearing</li>
      <li>Driveway / Footpath / Turf Prep</li>
      <li>Rubbish Removal</li>
      <li>Tree &amp; Stump removal</li>
    </ul>
    <ul class="services services--right">
      <li>Footings &amp; Post holes</li>
      <li>Drainage</li>
      <li>Service Installs</li>
      <li>Gravels &amp; Sands available</li>
      <li>Any general Earth moving needs</li>
      <li>Reliable Free Quotes</li>
      <li>Fully Insured</li>
    </ul>

    <div class="band band--red" style="top:288px;height:3px"></div>
    <div class="band band--navy" style="top:291px;height:69px"></div>
    <div class="contact" style="left:40px;top:300px">
      <svg width="22" height="18" viewBox="0 0 22 18" aria-hidden="true"><path d="M2 5 Q11 -1 20 5 L18 8 L15 6 L7 6 L4 8 Z M5 9 H17 L19 17 H3 Z" fill="var(--icon)"/></svg>
      <span>0438 605 312</span>
    </div>
    <div class="contact" style="left:300px;top:322px">
      <svg width="24" height="16" viewBox="0 0 24 16" aria-hidden="true"><rect x="1" y="1" width="22" height="14" fill="var(--icon)"/><path d="M1 1 L12 9 L23 1" fill="none" stroke="var(--navy)" stroke-width="1.5"/></svg>
      <span>owen.falkirk@tallmail.example</span>
    </div>
  </section>

</main>
</body>
</html>
```